Package Design for Plant-based Dumplings

We need a CPG Package design for a new product we're launching. I included example (front and back) of what a typical information food package has, so you can use it as reference.

Target Market(s)

Consumers that are seeking non-meat items. Environment concerned consumers.

Colors

Designer to choose colors to be used in the design.

Requirements
Must have
• Modern and clean looking design.
Nice to have
• might have multiple flavors, so make design where it could be have multiple variations.

```html
<!DOCTYPE html>
<html lang="en">
<head>
<meta charset="utf-8">
<title>Plant-Based Dumplings – Pouch Front</title>
<link rel="stylesheet" href="https://fonts.googleapis.com/css2?family=Kalam:wght@400;700&family=Roboto:wght@500;700&display=swap">
<style>
  :root {
    --backdrop: #d3d3d3;
    --pouch-black: #1c1a19;
    --orange: #e8902f;
    --brand-ink: #3a3532;
    --white: #f4f1ec;
    --line: rgba(255,255,255,0.55);
  }
  * { margin: 0; padding: 0; box-sizing: border-box; }
  html, body { width: 1200px; height: 800px; overflow: hidden; }
  body {
    background: var(--backdrop);
    font-family: "Kalam", cursive;
    position: relative;
  }
  .pouch {
    position: absolute;
    left: 391px; top: 82px;
    width: 410px; height: 648px;
    background: var(--pouch-black);
    border-radius: 20px;
    overflow: hidden;
    color: var(--white);
  }
  .pouch__band {
    position: absolute; left: 0; top: 0;
    width: 410px; height: 210px;
  }
  .pouch__notch {
    position: absolute; top: 42px;
    width: 6px; height: 6px; border-radius: 50%;
    background: var(--backdrop);
  }
  .pouch__notch--left { left: -3px; }
  .pouch__notch--right { right: -3px; }
  .pouch__zip {
    position: absolute; left: 18px; right: 18px; top: 79px;
    height: 5px;
    border-top: 1px solid rgba(0,0,0,0.12);
    border-bottom: 1px solid rgba(255,255,255,0.3);
  }
  .brand {
    position: absolute; left: 0; right: 0; top: 126px;
    text-align: center;
    font-family: "Kalam", cursive;
    font-weight: 700;
    font-size: 24px;
    line-height: 1.2;
    color: var(--brand-ink);
  }
  .product__kicker {
    position: absolute; left: 0; right: 0; top: 214px;
    text-align: center;
    font-size: 21px; letter-spacing: 4px; line-height: 1.2;
    color: var(--orange);
  }
  .product__name {
    position: absolute; left: 0; right: 0; top: 244px;
    text-align: center;
    font-weight: 700; font-size: 54px; letter-spacing: 1px;
    line-height: 1;
    color: var(--orange);
  }
  .product__tagline {
    position: absolute; left: 0; right: 0; top: 294px;
    text-align: center;
    font-size: 16px; letter-spacing: 0.5px; line-height: 1.2;
    color: var(--white);
  }
  .serving-photo {
    position: absolute; left: 65px; top: 336px;
    width: 276px; height: 276px; border-radius: 50%;
    background: radial-gradient(circle at 50% 48%, #8f8a6f 0%, #5d5a47 28%, #2a2826 58%, #151413 100%);
  }
  .claims {
    position: absolute; left: 322px; top: 395px;
    width: 66px;
    font-family: "Roboto", sans-serif;
    font-weight: 500; font-size: 7px;
    text-align: center; color: var(--white);
  }
  .claim { padding: 4px 0; }
  .claim + .claim { border-top: 1px solid var(--line); }
  .claim svg { display: block; margin: 3px auto 0; }
  .protein {
    position: absolute; left: 30px; top: 546px;
    font-family: "Roboto", sans-serif; color: var(--white);
  }
  .protein__amount { font-weight: 700; font-size: 30px; color: var(--orange); line-height: 1; }
  .protein__unit { font-size: 10px; font-weight: 500; }
  .storage {
    position: absolute; left: 42px; top: 598px;
    font-size: 16px; letter-spacing: 1px;
  }
  .net-weight {
    position: absolute; right: 52px; top: 600px;
    font-size: 14px; letter-spacing: 0.5px;
  }
</style>
</head>
<body>
  <main class="pouch">
    <svg class="pouch__band" viewBox="0 0 410 210" aria-hidden="true">
      <path d="M0 70 L300 0 L410 0 L410 115 L330 150 L250 168 L150 180 L70 192 L8 200 L0 130 Z" fill="var(--orange)"/>
    </svg>
    <span class="pouch__notch pouch__notch--left"></span>
    <span class="pouch__notch pouch__notch--right"></span>
    <div class="pouch__zip"></div>

    <p class="brand">Marlowe Foods</p>

    <p class="product__kicker">PLANT-BASED</p>
    <h1 class="product__name">DUMPLINGS</h1>
    <p class="product__tagline">Using Plant-based Meat and Vegetables</p>

    <div class="serving-photo" role="img" aria-label="Pan-fried dumplings with sesame seeds in a black cast-iron pan"></div>

    <div class="claims">
      <div class="claim">NO SOY
        <svg width="26" height="26" viewBox="0 0 26 26" aria-hidden="true">
          <circle cx="13" cy="13" r="8" fill="none" stroke="var(--white)" stroke-width="2"/>
          <line x1="3" y1="3" x2="23" y2="23" stroke="var(--white)" stroke-width="2"/>
        </svg>
      </div>
      <div class="claim">READY IN<br>MINUTES
        <svg width="34" height="26" viewBox="0 0 34 26" aria-hidden="true">
          <path d="M11 2 q2 3 0 6 M17 2 q2 3 0 6 M23 2 q2 3 0 6" fill="none" stroke="var(--white)" stroke-width="1.2"/>
          <path d="M4 13 H30 Q28 19 17 19 Q6 19 4 13 Z" fill="var(--white)"/>
          <line x1="10" y1="23" x2="24" y2="23" stroke="var(--white)" stroke-width="2"/>
        </svg>
      </div>
      <div class="claim">
        <svg width="34" height="34" viewBox="0 0 34 34" aria-hidden="true">
          <circle cx="17" cy="17" r="14" fill="none" stroke="var(--white)" stroke-width="2"/>
        </svg>
      </div>
    </div>

    <div class="protein">
      <span class="protein__amount">20g</span> <span class="protein__unit">of</span><br>
      <span class="protein__unit">Protein</span>
    </div>
    <p class="storage">Keep Frozen</p>
    <p class="net-weight">Net Wt. 2 LBs (32oz)</p>
  </main>
</body>
</html>
```